Calm and Clarity Health Flyer (new business startup)

One page...clear enough to be read if faxed. This mental health clinic treats depression/anxiety in kids and adults. It also treats opiate and alcohol addiction. It's in downtown Elmira, NY and the owner of the clinic is from Elmira NY, where it's located. This clinic does not take health insurance, so it charges a low rate of $75 a visit once they pay the $125 starting fee.

Target Market(s)

doctors offices, new patients

Industry/Entity Type

Doctor

Requirements
Must have
• see microsoft word document. pdf is printed on the company letterhead.
Nice to have
• a simplified map would be nice. if you can include the building it would be a plus. The same two fonts were used in the business cards and letter head (kennedy small caps boo*) and Refrigerator Delux.

```html
<!DOCTYPE html>
<html lang="en">
<head>
<meta charset="utf-8">
<title>Calm and Clarity Health Flyer</title>
<link href="https://fonts.googleapis.com/css2?family=Roboto+Condensed:wght@400;700&family=Lato:ital,wght@0,700;1,700&display=swap" rel="stylesheet">
<style>
  :root {
    --orange: #f0643a;
    --blue: #27a4de;
    --white: #ffffff;
    --ink: #2b2b2b;
    --slate: #474747;
    --pink: #f4a9a0;
    --map-land: #eceee9;
    --map-park: #d5ecd0;
    --map-water: #a9d3f2;
    --pin: #e2453a;
  }
  * { margin: 0; padding: 0; box-sizing: border-box; }
  html, body { width: 902px; height: 1200px; overflow: hidden; background: var(--white); }
  .flyer { position: relative; width: 902px; height: 1200px; background: var(--white); overflow: hidden; font-family: "Roboto Condensed", Arial, sans-serif; }
  .shapes { position: absolute; inset: 0; }
  .map { position: absolute; left: 353px; top: 790px; width: 549px; height: 410px; background: linear-gradient(180deg, var(--white) 0%, var(--map-land) 14%, var(--map-land) 38%, var(--map-park) 44%, var(--map-water) 52%, var(--map-water) 100%); }
  .map-pin { position: absolute; left: 537px; top: 890px; }
  .brand { position: absolute; left: 40px; top: 58px; display: flex; align-items: center; gap: 14px; }
  .brand-dot { width: 60px; height: 60px; border-radius: 50%; background: var(--orange); }
  .brand-name { font-weight: 700; font-size: 32px; color: var(--orange); letter-spacing: 0.2px; }
  .hours { position: absolute; left: 10px; width: 520px; top: 215px; text-align: center; color: var(--white); line-height: 1.1; }
  .hours-title { font-size: 60px; color: var(--slate); }
  .hours-line { font-size: 56px; }
  .ages { position: absolute; left: 475px; top: 348px; width: 210px; height: 210px; border-radius: 50%; background: var(--blue); border: 6px solid var(--white); color: var(--white); text-align: center; display: flex; flex-direction: column; justify-content: center; line-height: 1.12; }
  .ages-label { font-size: 30px; }
  .ages-value { font-size: 38px; }
  .ages-note { font-size: 30px; }
  .service { position: absolute; left: 0; width: 415px; text-align: center; color: var(--ink); }
  .service-icon { width: 76px; height: 76px; margin: 0 auto 10px; border-radius: 50%; background: var(--white); border: 4px solid var(--orange); display: flex; align-items: center; justify-content: center; }
  .service-icon span { display: block; width: 44px; height: 44px; border-radius: 50%; background: var(--ink); }
  .service-name { font-size: 30px; }
  .service-price { font-size: 23px; color: var(--white); margin-top: 8px; }
  .service-eval { top: 545px; }
  .service-visit { top: 720px; }
  .conditions { position: absolute; left: 462px; top: 578px; }
  .conditions-title { font-size: 27px; font-weight: 400; color: var(--ink); }
  .condition-list { position: absolute; top: 48px; list-style: none; font-family: "Lato", Arial, sans-serif; font-weight: 700; font-size: 21px; color: var(--ink); }
  .condition-list li { position: relative; padding-left: 36px; height: 39px; line-height: 1.15; }
  .condition-list li::before { content: ""; position: absolute; left: 0; top: 6px; width: 14px; height: 14px; border-radius: 50%; background: var(--orange); }
  .list-left { left: 7px; }
  .list-right { left: 188px; width: 230px; }
  .building { position: absolute; left: 90px; top: 897px; width: 262px; height: 262px; border-radius: 50%; border: 8px solid var(--orange); background: linear-gradient(180deg, #c9dcf0 0%, #a9604a 35%, #8a4e3c 80%, #9b9b9b 100%); }
  .footer { position: absolute; left: 432px; top: 1112px; width: 450px; color: var(--white); font-family: "Lato", Arial, sans-serif; font-weight: 700; }
  .footer-quote { font-style: italic; font-size: 15px; }
  .footer-note { font-style: italic; font-size: 11px; margin-top: 10px; line-height: 1.25; }
</style>
</head>
<body>
<div class="flyer">
  <div class="map" role="img" aria-label="Street map of the downtown clinic location by the river"></div>

  <svg class="shapes" width="902" height="1200" viewBox="0 0 902 1200" aria-hidden="true">
    <path d="M0,505 C150,525 330,530 470,522 C420,700 445,900 420,1150 L0,1150 Z" fill="var(--blue)"/>
    <path d="M0,245 C150,205 380,185 470,198 C545,215 545,480 470,515 C330,532 150,522 0,500 Z" fill="var(--orange)"/>
    <path d="M690,42 A205,205 0 0 1 880,420" fill="none" stroke="var(--blue)" stroke-width="10"/>
    <circle cx="704" cy="250" r="196" fill="var(--white)" stroke="var(--orange)" stroke-width="7"/>
    <polygon points="330,985 540,905 360,1060" fill="var(--orange)"/>
    <path d="M0,1140 C300,1085 600,1072 902,1088 L902,1200 L0,1200 Z" fill="var(--orange)"/>
  </svg>

  <svg class="map-pin" width="18" height="24" viewBox="0 0 18 24" aria-hidden="true">
    <path d="M9,0 C4,0 0,4 0,9 C0,15 9,24 9,24 C9,24 18,15 18,9 C18,4 14,0 9,0 Z" fill="var(--pin)"/>
    <circle cx="9" cy="9" r="3.5" fill="var(--white)"/>
  </svg>

  <div class="brand">
    <span class="brand-dot"></span>
    <span class="brand-name">CALM &amp; CLARITY HEALTH</span>
  </div>

  <div role="img" aria-label="Illustration of a head in profile with a brain" style="position:absolute;left:530px;top:76px;width:348px;height:348px;border-radius:50%;background:radial-gradient(circle at 60% 45%, var(--pink) 0%, #fbe1dc 55%, var(--white) 80%);"></div>

  <div class="hours">
    <div class="hours-title">HOURS:</div>
    <div class="hours-line">MONDAY</div>
    <div class="hours-line">AND SATURDAYS</div>
    <div class="hours-line">9-4PM</div>
  </div>

  <div class="ages">
    <div class="ages-label">Ages:</div>
    <div class="ages-value">6 years old</div>
    <div class="ages-note">and up</div>
  </div>

  <div class="service service-eval">
    <div class="service-icon" role="img" aria-label="Head with brain icon"><span></span></div>
    <div class="service-name">Psychiatric Evaluation</div>
    <div class="service-price">(45min)……………....$125*</div>
  </div>

  <div class="service service-visit">
    <div class="service-icon" role="img" aria-label="Two people seated in conversation icon"><span></span></div>
    <div class="service-name">Psychiatric Office Visit</div>
    <div class="service-price">(15min)………………..$75*</div>
  </div>

  <div class="conditions">
    <div class="conditions-title">Conditions Treated:</div>
    <ul class="condition-list list-left">
      <li>Depression</li>
      <li>Anxiety</li>
      <li>PTSD</li>
      <li>ADHD</li>
    </ul>
    <ul class="condition-list list-right">
      <li>Addiction</li>
      <li>Bipolar</li>
      <li>Childhood Mood Disorders</li>
    </ul>
  </div>

  <div class="building" role="img" aria-label="Photo of the brick clinic building"></div>

  <div class="footer">
    <div class="footer-quote">“We work for you, not the insurance companies”</div>
    <div class="footer-note">*Although we do not partner with any Health Insurance Companies at this time, a bill will be provided to you at the time of service for you to submit to your insurance company.</div>
  </div>
</div>
</body>
</html>
```